App Company Business Card Design Project

We are looking for a two sided business card design with one side in English and one side in Chinese. Information should include:
1. Name
2. Email
3. Cell phone
4. Address
Please incorporate the logo attached. Above are the only requirements.

Industry/Entity Type

Business

```html
<!DOCTYPE html>
<html lang="en">
<head>
<meta charset="utf-8">
<title>Kestrel Harbor — Business Card</title>
<link href="https://fonts.googleapis.com/css2?family=Arimo:wght@400;700&family=Cinzel:wght@400&display=swap" rel="stylesheet">
<style>
  :root {
    --page-bg: #f8f8f8;
    --card-light: #d5edf3;
    --card-dark: #444444;
    --ink-dark: #454545;
    --accent-orange: #e8873a;
    --accent-teal: #45b8c8;
    --text-light: #ffffff;
    --card-edge: #9a9a9a;
  }
  * { box-sizing: border-box; margin: 0; padding: 0; }
  html, body {
    width: 992px;
    height: 1200px;
    overflow: hidden;
    background: var(--page-bg);
  }
  .canvas {
    position: relative;
    width: 992px;
    height: 1200px;
  }
  .card {
    position: absolute;
    left: 67px;
    width: 862px;
    height: 491px;
    background: var(--card-light);
    border: 1px solid var(--card-edge);
    box-shadow: 8px 9px 8px rgba(0, 0, 0, 0.55);
    overflow: hidden;
  }
  .card--front { top: 66px; }
  .card--back { top: 621px; }

  .brand {
    position: absolute;
    display: flex;
    align-items: center;
    gap: 14px;
    font-family: "Arimo", Arial, sans-serif;
    font-weight: 700;
    font-size: 37px;
    letter-spacing: 2px;
    color: var(--ink-dark);
    text-transform: uppercase;
    white-space: nowrap;
  }
  .brand__mark {
    width: 26px;
    height: 26px;
    background: var(--accent-teal);
  }
  .card--front .brand { left: 210px; top: 58px; }
  .card--back .brand { left: 212px; top: 216px; }

  .info-band {
    position: absolute;
    left: 0;
    top: 198px;
    width: 100%;
    height: 293px;
    background: var(--card-dark);
  }
  .holder-name {
    position: absolute;
    left: 64px;
    top: 106px;
    font-family: "Cinzel", "Times New Roman", serif;
    font-size: 34px;
    color: var(--accent-orange);
    white-space: nowrap;
  }
  .divider {
    position: absolute;
    left: 359px;
    top: 22px;
    width: 2px;
    height: 236px;
    background: linear-gradient(to bottom, rgba(190,225,235,0) 0%, rgba(190,225,235,0.85) 50%, rgba(190,225,235,0) 100%);
  }
  .contact-list {
    position: absolute;
    left: 470px;
    top: 88px;
    list-style: none;
    font-family: "Arimo", Arial, sans-serif;
    font-size: 21px;
    color: var(--text-light);
  }
  .contact-list li {
    display: flex;
    align-items: center;
    height: 36px;
  }
  .contact-list svg {
    width: 22px;
    height: 22px;
    margin-right: 29px;
    fill: var(--text-light);
    flex: none;
  }
</style>
</head>
<body>
<main class="canvas">
  <section class="card card--front" aria-label="Business card front">
    <div class="brand"><span class="brand__mark"></span>Kestrel Harbor</div>
    <div class="info-band">
      <p class="holder-name">Your Name</p>
      <div class="divider"></div>
      <ul class="contact-list">
        <li>
          <svg viewBox="0 0 24 24" aria-hidden="true"><path d="M3 7h18v11H3z M3 7l9 6 9-6" fill="none" stroke="#fff" stroke-width="2"/><path d="M3 7h18l-9 6z"/></svg>
          Name@Your Email.com
        </li>
        <li>
          <svg viewBox="0 0 24 24" aria-hidden="true"><path d="M7 2l3 5-2 2c1 3 3 5 6 6l2-2 5 3-2 4C11 20 4 13 3 5z"/></svg>
          000-000-0000
        </li>
        <li>
          <svg viewBox="0 0 24 24" aria-hidden="true"><path d="M12 1a7 7 0 0 0-7 7c0 5 7 14 7 14s7-9 7-14a7 7 0 0 0-7-7zm0 10a3 3 0 1 1 0-6 3 3 0 0 1 0 6z"/></svg>
          Your Address
        </li>
      </ul>
    </div>
  </section>

  <section class="card card--back" aria-label="Business card back">
    <div class="brand"><span class="brand__mark"></span>Kestrel Harbor</div>
  </section>
</main>
</body>
</html>
```